Brindle Advisory Business Card Design

Business card for business consulting company, using attached logo. We do financial and strategic consulting, and want a clean, professional image with a bit of fun. Our logo is a flat whale tail, which symbolizes the Orca whale, a highly collaborative, group based animal that is very successful in navigating the ocean, protecting the herd, and hunting. We like the logo that is blue and gray on white one one side, but would be open to a blue card with white lettering on the other side... or whatever you'd suggest
Updates
Hi all - I have had the logo modified to take the shadowing off the tail. I will post it on the brief... under a file name called updated logo. thank you Added Saturday, April 25, 2015
Target Market(s)
Small to medium sized businesses ($10M to $500M in revenue per year), financial and sales executives, general managers, attorneys and CPAs
Industry/Entity Type
Financial
Contact Information for Business Card
Want company name, contact info - name, title, telephone, email, website, linkedin, twitter and Facebook. No physical address yet.
Requirements
Must have
- contemporary design, bold, strong, confident but with a bit of fun. prominently feature the logo and the whale tail icon
Nice to have
- unique touches that would differentiate us from a regular card... for example, logo and writing all on front on white background, but on back - logo in white on a blue background
- open to idea of different shapes of card than standard... but not sure
Should not have
- ?

```html
<!DOCTYPE html>
<html lang="en">
<head>
<meta charset="utf-8">
<title>Brindle Advisory – Business Card</title>
<link rel="stylesheet" href="https://fonts.googleapis.com/css2?family=Open+Sans:wght@400;600;700&display=swap">
<style>
  :root {
    --navy: #1f3a6b;
    --navy-deep: #1a3260;
    --grey: #9a9a9a;
    --white: #ffffff;
    --backdrop: #e9e9ec;
  }
  * { margin: 0; padding: 0; box-sizing: border-box; }
  html, body { width: 1200px; height: 1000px; overflow: hidden; }
  body {
    background: var(--backdrop);
    font-family: "Open Sans", Arial, sans-serif;
    position: relative;
  }
  .card {
    position: absolute;
    left: 265px;
    width: 667px;
    height: 397px;
    border-radius: 22px;
    overflow: hidden;
    box-shadow: 0 4px 14px rgba(0,0,0,0.18);
  }
  .card-front { top: 73px; background: var(--white); }
  .card-back { top: 533px; background: var(--navy); }

  .front-band {
    position: absolute; left: 0; bottom: 0;
    width: 100%; height: 32px; background: var(--navy);
  }

  .brand { position: absolute; }
  .brand-mark { position: absolute; border-radius: 6px; }
  .brand-name {
    position: absolute; white-space: nowrap;
    font-weight: 600; letter-spacing: -1px; line-height: 1;
  }
  .brand-tagline {
    position: absolute; white-space: nowrap;
    font-size: 12px; font-weight: 600; line-height: 1; text-align: right;
  }

  .card-front .brand-mark { left: 32px; top: 169px; width: 56px; height: 56px; background: var(--navy); }
  .card-front .brand-name { left: 96px; top: 174px; font-size: 37px; color: var(--navy); }
  .card-front .brand-tagline { right: 304px; top: 213px; color: var(--navy); }

  .card-back .brand-mark { left: 52px; top: 205px; width: 28px; height: 28px; background: var(--white); border-radius: 4px; }
  .card-back .brand-name { left: 96px; top: 195px; font-size: 37px; color: var(--white); }
  .card-back .brand-tagline { right: 304px; top: 230px; color: var(--white); }

  .divider {
    position: absolute; left: 394px; top: 105px;
    width: 2px; height: 195px;
    background: linear-gradient(to bottom, rgba(31,58,107,0), var(--navy) 30%, var(--navy) 70%, rgba(31,58,107,0));
  }

  .contact { position: absolute; left: 427px; top: 84px; }
  .contact-name { font-size: 18px; font-weight: 700; color: var(--navy); line-height: 24px; }
  .contact-title { font-size: 15px; color: var(--grey); line-height: 18px; }
  .contact-address { margin-top: 18px; font-size: 15.5px; color: var(--navy); line-height: 19px; }
  .contact-list { list-style: none; font-size: 15.5px; color: var(--grey); line-height: 19.5px; }
  .contact-list.primary { margin-top: 5px; }
  .contact-list.social { margin-top: 4px; }
  .contact-list li { display: flex; align-items: center; }
  .contact-list .icon { width: 13px; height: 13px; margin-right: 5px; flex: none; }
  .social-square { width: 12px; height: 12px; margin-right: 6px; background: var(--navy); border-radius: 2px; flex: none; }
</style>
</head>
<body>

  <section class="card card-front" aria-label="Card front">
    <div class="brand">
      <span class="brand-mark"></span>
      <span class="brand-name">brindleadvisory</span>
      <span class="brand-tagline">business consulting</span>
    </div>

    <div class="divider"></div>

    <div class="contact">
      <p class="contact-name">Daniel Hartwell</p>
      <p class="contact-title">Founder / CEO</p>
      <p class="contact-address">14 Larchmont Road<br>Greyvale VIC 3190</p>

      <ul class="contact-list primary">
        <li>
          <svg class="icon" viewBox="0 0 16 16" aria-hidden="true"><path fill="#1f3a6b" d="M1 6c0-2 3-4 7-4s7 2 7 4v1h-4V5.5C10 5 9 5 8 5s-2 0-3 .5V7H1z M4 8h8l2 6H2z"/></svg>
          999 999 9999
        </li>
        <li>
          <svg class="icon" viewBox="0 0 16 16" aria-hidden="true"><rect x="1" y="3" width="14" height="10" fill="#1f3a6b"/><path d="M1.5 3.5 8 9l6.5-5.5" stroke="#fff" stroke-width="1.3" fill="none"/></svg>
          info@brindleadvisory.com
        </li>
        <li>
          <svg class="icon" viewBox="0 0 16 16" aria-hidden="true"><g fill="none" stroke="#1f3a6b" stroke-width="1.3"><circle cx="8" cy="8" r="6.5"/><ellipse cx="8" cy="8" rx="3" ry="6.5"/><path d="M1.5 8h13M2.5 4.5h11M2.5 11.5h11"/></g></svg>
          www.brindleadvisory.com
        </li>
      </ul>

      <ul class="contact-list social">
        <li><span class="social-square"></span>brindleadvisory</li>
        <li><span class="social-square"></span>@brindleadvisory</li>
        <li><span class="social-square"></span>brindleadvisory</li>
      </ul>
    </div>

    <div class="front-band"></div>
  </section>

  <section class="card card-back" role="img" aria-label="Card back: navy field where a faint repeating whale-tail pattern belongs, with the company name in white">
    <div class="brand">
      <span class="brand-mark"></span>
      <span class="brand-name">brindleadvisory</span>
      <span class="brand-tagline">business consulting</span>
    </div>
  </section>

</body>
</html>
```